"Green Shopper Award" sales presentation

UK: "Shopper Award Green" is a French label, rewarding the best organic product sold in hyper and supermarkets. We already did the presentation in PPT format. But it is not design and professional-looking enough. The idea is that you use the existing document, and do not change anything in the structure, content, and text: you only have to improve the design (using the appropriate color code). We thank you in advance for any suggestion! FR: "Trophée Acheteurs Verts" is a French distinction that rewards the best organic products sold in supermarkets and hypermarkets. The sales pitch is already done in PPT version. However, he still does not look pretty design / professional. Thus, we do not want you to modify the content, the structure, the images, but simply that you make it more design (following the appropriate graphic). Thank you in advance for your feedback!

Target Market(s)

Organic brands and supermarkets / organic brands and supermarkets

Requirements
Must have
• Follow the structure of the PPT made available (see attachment), keep the structure and the content, but improve the design - ideally with illustrator Ideally use Illustrator (Adobe) to improve the design of the current presentation - purpose keep the same content and structure
Nice to have
• You can use Illustrator ideally (or photoshop) to rework the design of the PPT

```html
<!DOCTYPE html>
<html lang="fr">
<head>
<meta charset="utf-8">
<title>Trophée Acheteurs Verts 2019</title>
<link href="https://fonts.googleapis.com/css2?family=Montserrat:wght@500;600;700;800&family=Open+Sans:wght@400;600;700&display=swap" rel="stylesheet">
<style>
:root{
  --teal:#13706c;
  --teal-dark:#0d5b63;
  --pink:#e6336f;
  --pink-soft:#f7c4d4;
  --lime:#a3cc3a;
  --green:#4aa34a;
  --text:#5b5b5b;
  --line:#c9c9c9;
  --page:#ffffff;
}
*{box-sizing:border-box;margin:0;padding:0}
html,body{width:1200px;height:3000px;overflow:hidden;background:var(--page)}
body{font-family:"Open Sans",Arial,sans-serif;color:var(--text);position:relative}
.slide{position:absolute;left:90px;width:1020px;height:570px;background:#fff;overflow:hidden;box-shadow:0 2px 10px rgba(0,0,0,.12)}
.s1{top:0}.s2{top:610px}.s3{top:1210px}.s4{top:1810px}.s5{top:2410px}
.abs{position:absolute}
.cover-photo{position:absolute;inset:0;background:linear-gradient(100deg,#dfe9ea 0%,#e9eef0 40%,#f2e3d2 65%,#e7edf0 100%)}
.cover-overlay{position:absolute;inset:0;background:linear-gradient(105deg,rgba(18,120,112,.9) 0%,rgba(76,165,90,.82) 55%,rgba(160,205,60,.85) 100%)}
.cover-wave{position:absolute;left:0;top:0;width:1020px;height:570px}
.cover-title{position:absolute;left:50px;top:116px;font-family:Montserrat,sans-serif;font-weight:800;font-size:47px;line-height:1.17;letter-spacing:.5px}
.s1 .cover-title{background:linear-gradient(90deg,var(--lime),#5aa94a);-webkit-background-clip:text;background-clip:text;color:transparent}
.s2 .cover-title{color:#fff;left:62px;top:104px}
.brand{position:absolute;display:flex;align-items:center;gap:10px;font-family:Montserrat,sans-serif;font-weight:700}
.brand .mark-sq{width:40px;height:40px;background:var(--pink);border-radius:4px;flex:none}
.brand .mark-ci{width:34px;height:34px;border-radius:50%;background:var(--lime);flex:none}
.brand-client{color:var(--pink);font-size:18px;width:170px;line-height:1.1}
.brand-partner{color:var(--teal);font-size:26px;letter-spacing:1px}
.slide-title{position:absolute;left:36px;top:24px;font-family:Montserrat,sans-serif;font-weight:600;font-size:36px;color:var(--teal)}
.slide-title::after{content:"";position:absolute;left:0;top:54px;width:54px;height:4px;border-radius:2px;background:var(--pink)}
.footer-wave{position:absolute;left:0;bottom:0;width:1020px;height:40px}
.page-num{position:absolute;left:24px;bottom:14px;font-size:13px;color:#777}
.footer-brands{position:absolute;right:24px;bottom:14px;display:flex;align-items:center;gap:14px}
.footer-brands .brand{position:static;gap:6px}
.footer-brands .mark-sq{width:22px;height:22px}
.footer-brands .mark-ci{width:16px;height:16px}
.footer-brands .brand-client{font-size:10px;width:auto;white-space:nowrap}
.footer-brands .brand-partner{font-size:14px}
.toc{position:absolute;left:40px;top:160px;list-style:none}
.toc li{position:relative;height:41px;padding-left:26px;font-size:15px;color:#555;display:flex;align-items:center}
.toc .num{position:absolute;left:0;top:-2px;font-family:Montserrat,sans-serif;font-weight:800;font-size:30px;color:var(--pink-soft);opacity:.7;z-index:0}
.toc .label{position:relative;z-index:1}
.banner{position:absolute;left:510px;top:92px;width:486px;height:38px;background:var(--pink);color:#fff;font-family:Montserrat,sans-serif;font-weight:600;font-size:15px;display:flex;align-items:center;justify-content:center}
.brand-card{position:absolute;width:152px;height:100px;background:#fff;box-shadow:0 2px 8px rgba(0,0,0,.15);border-radius:4px;display:flex;align-items:center;justify-content:center;font-family:Montserrat,sans-serif;font-weight:700;font-size:16px;color:var(--teal-dark);text-align:center}
.timeline{position:absolute;left:40px;top:288px;width:940px;height:2px;background:var(--line)}
.dot{position:absolute;width:12px;height:12px;border-radius:50%;transform:translate(-50%,-50%)}
.dot.pink{background:#a5245a}.dot.green{background:#4ca06e}
.icon-circle{position:absolute;width:84px;height:84px;border-radius:50%;transform:translate(-50%,-50%);display:flex;align-items:center;justify-content:center}
.icon-circle.ring{background:#fff;border:4px solid #f4d2dd}
.icon-circle.ring .core{width:62px;height:62px;border-radius:50%;background:var(--pink);display:flex;align-items:center;justify-content:center}
.icon-circle.solid{background:var(--pink);box-shadow:0 0 0 6px #fbe0e8}
.info{position:absolute;font-size:11.5px;line-height:1.4;color:#666}
.info b{color:#333}
.chart{position:absolute;left:644px;top:252px;width:174px;height:110px;background:#fafafa;border:1px solid #e2e2e2}
.badge-flat{position:absolute;left:826px;top:282px;width:46px;height:60px;background:#2d2d2d;border-radius:3px}
.caption{position:absolute;left:644px;top:372px;font-size:11px;color:#555;line-height:1.35}
.crit{position:absolute;width:360px}
.crit h3{font-family:"Open Sans",sans-serif;font-weight:700;font-size:16px;color:var(--pink);margin-bottom:2px}
.crit p{font-size:12px;line-height:1.4;color:#666}
.crit p b{color:#444}
.label-badges{position:absolute;left:620px;top:300px;display:flex;gap:18px;align-items:center}
.label-badges span{display:block;width:34px;height:34px;border-radius:50%;border:2px solid #8cbf4a}
.label-badges span.sq{border-radius:3px;background:#5aaa3c;border:none}
.products{position:absolute;left:50px;top:362px;width:560px;height:160px;border-radius:6px;background:linear-gradient(90deg,#e9b25a 0%,#d98a45 30%,#e8d7b4 55%,#cfb27a 80%,#b98654 100%)}
</style>
</head>
<body>

<section class="slide s1">
  <div class="cover-photo" role="img" aria-label="Photo d'une cliente souriante appuyée sur un chariot dans un rayon de supermarché"></div>
  <svg class="cover-wave" viewBox="0 0 1020 570" preserveAspectRatio="none" aria-hidden="true">
    <path d="M0 392 C220 350 420 468 650 438 C820 416 930 370 1020 360 L1020 570 L0 570 Z" fill="#fff"/>
    <path d="M0 392 C220 350 420 468 650 438 C820 416 930 370 1020 360 L1020 374 C930 388 820 430 650 452 C420 482 220 368 0 404 Z" fill="#1f8a6c"/>
  </svg>
  <h1 class="cover-title">SELECTION<br>ACHETEURS<br>VERTS 2019</h1>
  <div class="brand" style="left:34px;top:426px"><span class="mark-sq"></span><span class="brand-client">Trophée Acheteurs Verts</span></div>
  <div class="abs" style="left:256px;top:420px;width:1px;height:62px;background:#ccc"></div>
  <div class="brand" style="left:282px;top:434px"><span class="mark-ci"></span><span class="brand-partner">VERDALIS</span></div>
</section>

<section class="slide s2">
  <div class="cover-photo" role="img" aria-label="Photo d'une cliente souriante appuyée sur un chariot dans un rayon de supermarché"></div>
  <div class="cover-overlay"></div>
  <svg class="cover-wave" viewBox="0 0 1020 570" preserveAspectRatio="none" aria-hidden="true">
    <path d="M0 400 C220 360 420 470 650 440 C820 418 930 372 1020 362 L1020 570 L0 570 Z" fill="#fff"/>
    <path d="M0 400 C220 360 420 470 650 440 C820 418 930 372 1020 362 L1020 376 C930 390 820 432 650 454 C420 484 220 376 0 412 Z" fill="#1f8a6c"/>
  </svg>
  <h1 class="cover-title">SELECTION<br>ACHETEURS<br>VERTS 2019</h1>
  <div class="brand" style="left:34px;top:430px"><span class="mark-sq"></span><span class="brand-client">Trophée Acheteurs Verts</span></div>
  <div class="abs" style="left:256px;top:424px;width:1px;height:62px;background:#ccc"></div>
  <div class="brand" style="left:282px;top:438px"><span class="mark-ci"></span><span class="brand-partner">VERDALIS</span></div>
</section>

<section class="slide s3">
  <h2 class="slide-title">Sommaire</h2>
  <ol class="toc">
    <li><span class="num">01</span><span class="label">Trophée Acheteurs Verts, c'est quoi?</span></li>
    <li><span class="num">02</span><span class="label">Une certification d'excellence</span></li>
    <li><span class="num">03</span><span class="label">Qui peut concourir?</span></li>
    <li><span class="num">04</span><span class="label">Le déroulement du concours</span></li>
    <li><span class="num">05</span><span class="label">Participer, c'est...</span></li>
    <li><span class="num">06</span><span class="label">La visibilité des lauréats</span></li>
    <li><span class="num">07</span><span class="label">Inscription</span></li>
  </ol>
  <div class="banner">Les marques participantes de l'édition 2018</div>
  <div class="brand-card" style="left:504px;top:158px">Rucher Doré</div>
  <div class="brand-card" style="left:676px;top:158px">Verdane</div>
  <div class="brand-card" style="left:850px;top:158px">Pain Solaire</div>
  <div class="brand-card" style="left:504px;top:272px">Potager Clair</div>
  <div class="brand-card" style="left:676px;top:272px">Olvana</div>
  <div class="brand-card" style="left:850px;top:272px">Tiloa</div>
  <div class="brand-card" style="left:590px;top:386px">Prairie Douce</div>
  <div class="brand-card" style="left:762px;top:386px">Ciel de Miel</div>
  <svg class="footer-wave" viewBox="0 0 1020 40" preserveAspectRatio="none" aria-hidden="true"><path d="M0 22 C300 6 600 36 1020 12 L1020 40 L0 40 Z" fill="#e7f1da"/></svg>
  <span class="page-num">3</span>
  <div class="footer-brands"><div class="brand"><span class="mark-sq"></span><span class="brand-client">Trophée Acheteurs Verts</span></div><div class="brand"><span class="mark-ci"></span><span class="brand-partner">VERDALIS</span></div></div>
</section>

<section class="slide s4">
  <h2 class="slide-title">Trophée Acheteurs Verts, c'est quoi?</h2>
  <div class="timeline"></div>
  <span class="dot pink" style="left:110px;top:289px"></span>
  <span class="dot green" style="left:266px;top:289px"></span>
  <span class="dot pink" style="left:426px;top:289px"></span>
  <span class="dot pink" style="left:586px;top:289px"></span>

  <div class="icon-circle ring" style="left:266px;top:190px"><span class="core"><svg width="30" height="30" viewBox="0 0 30 30"><rect x="5" y="6" width="20" height="18" rx="2" fill="#fff"/><rect x="9" y="11" width="12" height="8" fill="#e6336f"/></svg></span></div>
  <div class="icon-circle ring" style="left:586px;top:190px"><span class="core"><svg width="30" height="30" viewBox="0 0 30 30"><circle cx="15" cy="12" r="8" fill="none" stroke="#fff" stroke-width="2.5"/><path d="M10 18 L8 28 L15 24 L22 28 L20 18" fill="none" stroke="#fff" stroke-width="2.5"/></svg></span></div>
  <div class="icon-circle solid" style="left:110px;top:384px"><svg width="38" height="38" viewBox="0 0 38 38"><circle cx="19" cy="9" r="4" fill="#fff"/><circle cx="9" cy="25" r="4" fill="#fff"/><circle cx="29" cy="25" r="4" fill="#fff"/><path d="M19 14v6M9 20h20" stroke="#fff" stroke-width="2"/></svg></div>
  <div class="icon-circle solid" style="left:426px;top:384px"><svg width="34" height="34" viewBox="0 0 34 34"><rect x="7" y="4" width="20" height="26" rx="2" fill="none" stroke="#fff" stroke-width="2.5"/><path d="M11 12h12M11 18h12M11 24h7" stroke="#fff" stroke-width="2"/></svg></div>

  <p class="info" style="left:320px;top:110px;width:190px">Ce concours distingue les produits bio et les produits écologiques les mieux notés du circuit GMS, afin d'encourager l'excellence dans ce secteur et aiguiller les consommateurs dans leurs achats.</p>
  <p class="info" style="left:644px;top:82px;width:200px">La distinction Trophée Acheteurs Verts est calquée sur le même modèle que notre distinction Top Produits Verts qui est elle dédiée au circuit spécialisé. Cette dernière, lancée en 2013, est très largement plébiscitée par les consommateurs.</p>
  <p class="info" style="left:164px;top:352px;width:180px">C'est la <b>distinction de consommateurs</b> réservée aux produits bio commercialisés en <b>GMS</b> (Grande et Moyenne Surface).</p>
  <p class="info" style="left:478px;top:352px;width:150px">Elle permet d'identifier les produits d'excellence de la filière biologique en circuit GMS, les mettre en avant et stimuler leurs ventes et augmenter leur notoriété.</p>

  <svg class="chart" viewBox="0 0 174 110" aria-label="Graphique d'enquête en barres">
    <rect x="8" y="10" width="150" height="10" fill="#9cc6e8"/><rect x="8" y="10" width="150" height="10" fill="none" stroke="#e6336f" stroke-width="1.5"/>
    <rect x="8" y="28" width="112" height="10" fill="#9cc6e8"/>
    <rect x="8" y="46" width="88" height="10" fill="#9cc6e8"/>
    <rect x="8" y="64" width="70" height="10" fill="#9cc6e8"/>
    <rect x="8" y="82" width="52" height="10" fill="#9cc6e8"/>
  </svg>
  <div class="badge-flat"></div>
  <p class="caption">Enquête Panel Conso,<br>décembre 2017</p>

  <svg class="footer-wave" viewBox="0 0 1020 40" preserveAspectRatio="none" aria-hidden="true"><path d="M0 22 C300 6 600 36 1020 12 L1020 40 L0 40 Z" fill="#e7f1da"/></svg>
  <span class="page-num">4</span>
  <div class="footer-brands"><div class="brand"><span class="mark-sq"></span><span class="brand-client">Trophée Acheteurs Verts</span></div><div class="brand"><span class="mark-ci"></span><span class="brand-partner">VERDALIS</span></div></div>
</section>

<section class="slide s5">
  <h2 class="slide-title">Qui peut concourir?</h2>

  <div class="icon-circle solid" style="left:96px;top:166px"><svg width="38" height="38" viewBox="0 0 38 38"><circle cx="19" cy="9" r="4" fill="#fff"/><circle cx="9" cy="25" r="4" fill="#fff"/><circle cx="29" cy="25" r="4" fill="#fff"/><path d="M19 14v6M9 20h20" stroke="#fff" stroke-width="2"/></svg></div>
  <div class="crit" style="left:152px;top:140px;width:300px"><h3>Circuit GMS</h3><p>Pour participer il est nécessaire que les produits présentés ne soient vendus qu'en <b>circuit GMS</b>.</p></div>

  <div class="icon-circle solid" style="left:96px;top:292px"><svg width="38" height="38" viewBox="0 0 38 38"><path d="M4 20 L12 12 L19 16 L26 12 L34 20 L24 28 L14 28 Z" fill="none" stroke="#fff" stroke-width="2.5" stroke-linejoin="round"/></svg></div>
  <div class="crit" style="left:152px;top:266px;width:300px"><h3>Marques indépendantes</h3><p>Les <b>marques indépendantes</b> et les MDD peuvent désormais participer au concours.</p></div>

  <div class="icon-circle solid" style="left:566px;top:166px"><svg width="34" height="34" viewBox="0 0 30 30"><circle cx="15" cy="12" r="8" fill="none" stroke="#fff" stroke-width="2.5"/><path d="M10 18 L8 28 L15 24 L22 28 L20 18" fill="none" stroke="#fff" stroke-width="2.5"/></svg></div>
  <div class="crit" style="left:624px;top:140px;width:360px"><h3>Produits labelisés</h3><p>Cette distinction est uniquement destinée à des <b>produits labellisés</b>. Les labels retenus sont les suivants : Terre Saine (Agriculture Biologique), Alpa Bio Garantie, Vivea, Bio Racines, Bio Partage, Bio Horizon, Bio Entraide, Solvital, Cosmeva, Terrea, Ecoveris, Naturem, Nature &amp; Avenir, Sol Commun, Verdi Organic, Ecomarque.</p></div>

  <div class="label-badges" aria-label="Labels de certification">
    <span></span><span></span><span></span><span></span><span class="sq"></span><span class="sq"></span><span></span>
  </div>

  <div class="products" role="img" aria-label="Photo d'une sélection de produits bio lauréats : pots de miel, biscuits, sachets de graines et conserves"></div>

  <svg class="footer-wave" viewBox="0 0 1020 40" preserveAspectRatio="none" aria-hidden="true"><path d="M0 22 C300 6 600 36 1020 12 L1020 40 L0 40 Z" fill="#e7f1da"/></svg>
  <span class="page-num">6</span>
  <div class="footer-brands"><div class="brand"><span class="mark-sq"></span><span class="brand-client">Trophée Acheteurs Verts</span></div><div class="brand"><span class="mark-ci"></span><span class="brand-partner">VERDALIS</span></div></div>
</section>

</body>
</html>
```